Fresh Start Credit Guide - Banner Ad for CA Website

I need a banner ad for a book I'm selling.

The book is about Fresh Start Credit Guide, that is a County Court Judgment, from a credit report.

I have two websites. I want the banner ad to appear on
www.cardenashby.co.uk

It will then link to the new site: https://freshstartcreditguide.co.uk/

The first site already has a lot of traffic from visitors wanting to remove a CCJ. The purpose of that first site was originally for visitors to become clients of the law firm. However, most visitors can't afford legal advice and so I'd like to offer them the book instead.

I would like to see designs that use the colour green. The final design should communicate financial freedom, simplicity and trustworthiness.

Target Market(s)

Individuals who have discovered a CCJ on their credit report

Industry/Entity Type

Law

Font styles to use
Sans Serif

Colors
0054AA
0677BA
7BADD7
CADEEF
E8F1F8
0094D4
00A9DD
6FCCEA
C7EBF8
E9F6FB
00AB8E
00BBA5
67D7C9
C6EFE9
E9F9F6

Requirements
Must have
• Must fit at the end of a blog article, such as this one https://www.cardenashby.co.uk/ccj-wrong-address/

```html
<!DOCTYPE html>
<html lang="en">
<head>
<meta charset="utf-8">
<title>Fresh Start Credit Guide – Banner</title>
<link href="https://fonts.googleapis.com/css2?family=Montserrat:wght@600;700;800;900&display=swap" rel="stylesheet">
<style>
  :root {
    --page-bg: #e6e6e6;
    --green: #43a145;
    --green-light: #4eae4f;
    --green-shadow: #2b7a2e;
    --red: #ef2a2b;
    --red-dark: #bf171a;
    --white: #ffffff;
    --orange: #f09009;
    --device-dark: #232323;
    --cover-white: #fafafa;
    --cover-tint: #f6d9d9;
  }
  html, body {
    margin: 0;
    width: 1200px;
    height: 800px;
    overflow: hidden;
    background: var(--page-bg);
    font-family: "Montserrat", sans-serif;
  }
  .banner {
    position: absolute;
    left: 103px;
    top: 195px;
    width: 994px;
    height: 409px;
    overflow: hidden;
    background: var(--green);
  }
  .banner-bg { position: absolute; inset: 0; }
  .headline {
    position: absolute;
    left: 0;
    top: 0;
    margin: 0;
    color: var(--white);
    font-weight: 800;
    text-shadow: 2px 3px 0 var(--green-shadow);
  }
  .headline span { position: absolute; white-space: nowrap; line-height: 1; }
  .headline .need { left: 124px; top: 44px; font-size: 44px; }
  .headline .remove { left: 58px; top: 80px; font-size: 90px; letter-spacing: -2px; }
  .headline .article { left: 444px; top: 124px; font-size: 32px; }
  .headline .ccj { left: 124px; top: 160px; font-size: 96px; letter-spacing: -1px; }
  .tagline {
    position: absolute;
    left: 62px;
    top: 251px;
    padding-left: 17px;
    border-left: 2px solid var(--white);
    color: var(--white);
    font-weight: 700;
    font-size: 19px;
    line-height: 24px;
    margin: 0;
  }
  .cta {
    position: absolute;
    left: 62px;
    top: 326px;
    width: 224px;
    height: 38px;
    border: 2px solid var(--white);
    border-radius: 22px;
    background: var(--orange);
    color: var(--white);
    font-weight: 700;
    font-size: 18px;
    line-height: 38px;
    text-align: center;
    text-decoration: none;
  }
  .product { position: absolute; display: block; }
  .product-tablet { left: 502px; top: 87px; width: 186px; height: 275px; }
  .product-phone { left: 617px; top: 176px; width: 103px; height: 203px; }
  .product-book { left: 682px; top: 32px; width: 216px; height: 342px; }
</style>
</head>
<body>
  <section class="banner" aria-label="Fresh Start Credit Guide book banner">
    <svg class="banner-bg" width="994" height="409" viewBox="0 0 994 409" aria-hidden="true">
      <polygon points="0,178 210,409 0,409" fill="var(--green-light)"/>
      <polygon points="450,0 994,0 994,409 700,409" fill="var(--red)"/>
      <polygon points="450,0 523,0 556,175" fill="var(--red-dark)"/>
      <ellipse cx="760" cy="378" rx="190" ry="8" fill="#000" opacity="0.12"/>
    </svg>

    <h1 class="headline">
      <span class="need">Need to</span>
      <span class="remove">Remove</span>
      <span class="article">a</span>
      <span class="ccj">CCJ?</span>
    </h1>

    <p class="tagline">Find out how<br>with this simple jargon-free guide</p>

    <a class="cta" href="https://freshstartcreditguide.co.uk/">Get Your Copy Now</a>

    <defs></defs>
    <svg class="product product-tablet" viewBox="0 0 186 275" role="img" aria-label="Tablet showing the ebook cover of the guide">
      <defs>
        <linearGradient id="screenTone" x1="0" y1="0" x2="0" y2="1">
          <stop offset="0" stop-color="var(--cover-white)"/>
          <stop offset="1" stop-color="var(--cover-tint)"/>
        </linearGradient>
      </defs>
      <rect width="186" height="275" rx="10" fill="var(--device-dark)"/>
      <rect x="22" y="24" width="142" height="225" fill="url(#screenTone)"/>
    </svg>
    <svg class="product product-book" viewBox="0 0 216 342" role="img" aria-label="Paperback copy of the guide with its red and white cover">
      <defs>
        <linearGradient id="bookTone" x1="0" y1="0" x2="0" y2="1">
          <stop offset="0" stop-color="var(--cover-white)"/>
          <stop offset="1" stop-color="var(--cover-tint)"/>
        </linearGradient>
      </defs>
      <rect width="198" height="342" fill="url(#bookTone)"/>
      <polygon points="198,0 216,6 216,336 198,342" fill="#e4ddd3"/>
    </svg>
    <svg class="product product-phone" viewBox="0 0 103 203" role="img" aria-label="Smartphone showing the ebook cover of the guide">
      <defs>
        <linearGradient id="phoneScreen" x1="0" y1="0" x2="0" y2="1">
          <stop offset="0" stop-color="var(--cover-white)"/>
          <stop offset="1" stop-color="var(--cover-tint)"/>
        </linearGradient>
      </defs>
      <rect width="103" height="203" rx="12" fill="var(--device-dark)"/>
      <rect x="5" y="22" width="93" height="158" fill="url(#phoneScreen)"/>
    </svg>
  </section>
</body>
</html>
```